We are Pacific Auto Freight Traders from Japan to NewZealand

we are importing Japanese used cars from Japan to NewZealand and Motor vehicle parts trading in the world. we have company in Japan and New Zealand. we provide one stop service to import car from japan. we have two companies called PAF Ltd for car importing from japan and PAF Lubricants Ltd for car engine oil importing. also we are importing car parts under PAF Autohaus Ltd. we need logo and name card for our company. Company name is PAF LTD (Pacific Auto Freight Traders) From japan we are sourcing newer European cars and 20-30 years old special sports limited model cars importing specialist. we are not normal car importer and retailer. also we are manufacture and supplying Motor vehicle Engine oil and parts from Korea and japan to New Zealand. Engine oil and part brand name is 'Ultra Z' we would like to introduce on business card. we want to show what we are doing as car importing, selling, parts and engine oil importing.

Target Market(s)

-Car buyer(customer)
-Mechanic shop
-Car dealers
-Car industry people
-Car & parts exporter/importer
-Engine oil reseller
-parts reseller

Industry/Entity Type

Car Dealer

Contact Information for Business Card

Dale Ferro
Director
17 Brook Lane, Tokomai Flats, Auckland 0619, New Zealand
+64215093381
paf.limited@examplemail.co.nz
www.pafmotors-demo.co.nz
www.pafjapan-demo.com

Colors
ffc214
9d9d9d
0255a3

Requirements
Must have
• * PAF Motors Ltd(PAF LTD-car importing, sourcing and retailing)
• * PAF Lubricants Ltd(Engine Oil importing, sourcing and retailing)
• * PAF Autohaus Ltd(car parts and accessories importing, sourcing and retailing)
• * Ultra Z -Brand name of engine oil
• (We are wanting to make logo for PAF MOTORS and ULTRA Z MOTOR OIL)
Nice to have
• we would like to show us to our clients as professional, trustworthy, many experience. not well known in the market but unique indivisual company for clients.
Should not have
• we do not want to feel just 'car dealer' , 'importer' or normal sales

```html
<!DOCTYPE html>
<html lang="en">
<head>
<meta charset="utf-8">
<title>PAF Motors Ltd – Business Card</title>
<link rel="stylesheet" href="https://fonts.googleapis.com/css2?family=Open+Sans:wght@400;600&display=swap">
<style>
  :root {
    --bg: #4a423d;
    --card-dark: #141414;
    --card-mid: #262626;
    --yellow: #ffd21f;
    --grey: #9d9d9d;
    --light-grey: #c8c8c8;
    --white: #f2f2f2;
  }
  * { box-sizing: border-box; margin: 0; padding: 0; }
  html, body { width: 1200px; height: 844px; overflow: hidden; }
  body {
    background: var(--bg);
    font-family: "Open Sans", sans-serif;
    display: flex;
    align-items: center;
    justify-content: center;
    gap: 40px;
  }
  .card {
    position: relative;
    width: 540px;
    height: 300px;
    background: radial-gradient(ellipse at 50% 35%, var(--card-mid), var(--card-dark) 70%);
    overflow: hidden;
    box-shadow: 0 10px 30px rgba(0,0,0,0.45);
  }

  /* Contact side */
  .card--contact .band {
    position: absolute;
    left: 0; right: 0;
    height: 12px;
    background: var(--yellow);
  }
  .card--contact .band--top { top: 0; }
  .card--contact .band--bottom { bottom: 0; }
  .person {
    position: absolute;
    top: 48px;
    left: 0; right: 0;
    text-align: center;
  }
  .person__name {
    display: inline-block;
    color: var(--yellow);
    font-weight: 600;
    font-size: 17px;
    letter-spacing: 0.5px;
    padding: 0 14px 2px;
    border-bottom: 1px solid var(--light-grey);
  }
  .person__role {
    color: var(--white);
    font-size: 12px;
    margin-top: 2px;
  }
  .contacts {
    position: absolute;
    top: 122px;
    left: 0; right: 0;
    list-style: none;
    text-align: center;
    color: var(--white);
    font-size: 14px;
    line-height: 1.45;
  }
  .address {
    position: absolute;
    bottom: 28px;
    left: 0; right: 0;
    text-align: center;
    color: var(--white);
    font-size: 14px;
  }

  /* Brand side */
  .tab {
    position: absolute;
    width: 22px;
    height: 38px;
    background: linear-gradient(90deg, var(--yellow) 0 70%, var(--light-grey) 70% 100%);
  }
  .tab--left { left: 0; top: 112px; }
  .tab--right { right: 0; top: 24px; }
  .brand {
    position: absolute;
    top: 100px;
    left: 0; right: 0;
    text-align: center;
  }
  .brand__name {
    display: inline-flex;
    align-items: center;
    gap: 10px;
    color: var(--light-grey);
    font-weight: 600;
    font-size: 28px;
    letter-spacing: 1px;
  }
  .brand__mark {
    width: 14px;
    height: 14px;
    border-radius: 50%;
    background: var(--yellow);
  }
  .brand__full {
    color: var(--grey);
    font-size: 9px;
    margin-top: 2px;
  }
  .divisions {
    position: absolute;
    top: 188px;
    left: 0; right: 0;
    text-align: center;
    color: var(--white);
    font-size: 13px;
    line-height: 1.6;
  }
  .divisions__sep { padding: 0 6px; }
</style>
</head>
<body>
  <section class="card card--contact" aria-label="Business card, contact side">
    <div class="band band--top"></div>
    <div class="person">
      <div class="person__name">DALE FERRO</div>
      <div class="person__role">Director</div>
    </div>
    <ul class="contacts">
      <li>+64215093381</li>
      <li>paf.limited@examplemail.co.nz</li>
      <li>www.pafmotors-demo.co.nz</li>
      <li>www.pafjapan-demo.com</li>
    </ul>
    <p class="address">17 Brook Lane, Tokomai Flats, Auckland 0619, New Zealand</p>
    <div class="band band--bottom"></div>
  </section>

  <section class="card card--brand" aria-label="Business card, brand side">
    <div class="tab tab--right"></div>
    <div class="tab tab--left"></div>
    <div class="brand">
      <div class="brand__name"><span>PAF MOTORS LTD</span><span class="brand__mark"></span></div>
      <div class="brand__full">Pacific Auto Freight Traders Limited (PAFT)</div>
    </div>
    <div class="divisions">
      <div>PAF Motors Ltd<span class="divisions__sep">|</span>PAF Lubricants Ltd<span class="divisions__sep">|</span>PAF Autohaus Ltd</div>
      <div>Ultra Z-Brand name of engine oil</div>
    </div>
  </section>
</body>
</html>
```